Business Card Design

We would like to re-design our business cards. Our Company - Qoralin Turbochargers, rebuilds turbochargers and sells replacement parts. Our website is: http://www.qoralinturbochargers-example.com
We just had our logo changed. I will attach the file. Looking for fresh new/modern business card. We like the colors red, black, white and silver. Black background looks attractive, but not a requirement. The final design should communicate reasonable/competitive prices, top quality and reliability of our products.
Updates
Project Deadline Extended
Reason: Need to finalize the info on the card. Currently working on changing address and email info. Want to make sure it is the correct one before accepting the final design. Unless, this is something that can be changed at a later time..??
Industry/Entity Type
Business
Contact Information for Business Card
QORALIN TURBOCHARGERS, LLC
20473 Pemberly Road NE
Massillon, OH 44012
Tel: +1-330-555-0162
Fax: +1-330-555-0187
info@QoralinTurbochargers-example.com
Our current business card had the following highlights:
*We rebuild all Turbocharges for Automotive, Diesel and Industrial
*Precision Balancing and in-house turbocharger needs
*All Turbocharger replacement parts are made in USA / U.K.
Look and feel
Each slider illustrates characteristics of the customer's brand and the style your logo design should communicate.

```html
<!DOCTYPE html>
<html lang="en">
<head>
<meta charset="utf-8">
<title>Qoralin Turbochargers – Business Card</title>
<link rel="stylesheet" href="https://fonts.googleapis.com/css2?family=Questrial&display=swap">
<style>
  :root {
    --page: #ffffff;
    --silver-light: #ececec;
    --silver-mid: #d2d2d2;
    --frame-fill: #e9e9e9;
    --graphite: #58585a;
    --graphite-band: #6a6a6c;
    --graphite-ghost: #666668;
    --ink: #1a1a1a;
    --ink-soft: #555557;
    --racing-red: #e41e26;
    --paper-text: #f2f2f2;
    --rule: #b8b8b8;
  }
  * { margin: 0; padding: 0; box-sizing: border-box; }
  html, body {
    width: 1002px; height: 1200px; overflow: hidden;
    background: var(--page);
    font-family: "Questrial", sans-serif;
  }
  .canvas { position: relative; width: 1002px; height: 1200px; }

  .card { position: absolute; left: 0; width: 1002px; border-radius: 24px; overflow: hidden; }

  /* Front */
  .card--front {
    top: 0; height: 573px;
    background: radial-gradient(ellipse at 50% 35%, var(--silver-light) 0%, var(--silver-mid) 80%);
  }
  .stripe { position: absolute; left: 0; width: 100%; }
  .card--front .stripe--wide { top: 234px; height: 41px; background: var(--graphite); }
  .card--front .stripe--thin { top: 283px; height: 19px; background: var(--graphite); }

  .brand-plate {
    position: absolute; left: 76px; top: 204px; width: 850px; height: 163px;
    background: var(--frame-fill);
    border: 3px solid var(--ink-soft);
    border-radius: 14px;
    display: flex; flex-direction: column; align-items: center; justify-content: center;
    gap: 14px;
  }
  .brand-name {
    display: flex; align-items: center; gap: 18px;
    font-size: 58px; color: var(--ink); letter-spacing: 1px; line-height: 1;
  }
  .brand-mark { width: 40px; height: 40px; background: var(--racing-red); }
  .brand-tagline { font-size: 19px; color: var(--ink); }

  .website {
    position: absolute; left: 0; top: 525px; width: 100%;
    text-align: center; font-size: 23px; color: var(--ink-soft);
  }

  /* Back */
  .card--back { top: 627px; height: 573px; background: var(--graphite); }
  .ghost-name {
    position: absolute; left: 0; top: 105px; width: 100%;
    text-align: center; font-size: 78px; color: var(--graphite-ghost);
    letter-spacing: 2px; line-height: 1;
  }
  .card--back .stripe--wide { top: 235px; height: 41px; background: var(--graphite-band); }
  .card--back .stripe--thin { top: 284px; height: 19px; background: var(--graphite-band); }

  .contact {
    position: absolute; left: 0; width: 100%; text-align: center; color: var(--paper-text);
  }
  .contact__name { top: 332px; font-size: 29px; }
  .contact__role { top: 370px; font-size: 29px; }
  .contact__reach { top: 407px; font-size: 25px; left: -20px; }
  .contact__rule {
    position: absolute; left: 55px; top: 472px; width: 892px; height: 2px; background: var(--rule);
  }
  .contact__company { top: 486px; font-size: 25px; }
</style>
</head>
<body>
<main class="canvas">
  <section class="card card--front" aria-label="Card front">
    <div class="stripe stripe--wide"></div>
    <div class="stripe stripe--thin"></div>
    <div class="brand-plate">
      <div class="brand-name"><span class="brand-mark"></span>Qoralin Turbochargers</div>
      <p class="brand-tagline">Rebuilds turbochargers and sells replacement parts.</p>
    </div>
    <p class="website">www.qoralinturbochargers-example.com</p>
  </section>

  <section class="card card--back" aria-label="Card back">
    <div class="ghost-name" aria-hidden="true">Qoralin Turbochargers</div>
    <div class="stripe stripe--wide"></div>
    <div class="stripe stripe--thin"></div>
    <p class="contact contact__name">Employee Name</p>
    <p class="contact contact__role">Designation</p>
    <p class="contact contact__reach">Contact no. / e-mail id</p>
    <div class="contact__rule"></div>
    <p class="contact contact__company">Company Address / Contact Contact&nbsp; No.</p>
  </section>
</main>
</body>
</html>
```